Promotion for Local Garage - KWB Motors offering 10% off

We are after an A5 Colour Leaflet to promote our business KWB Motors.

KWB Motors is a local garage and we are about to launch a flyer campaign in the local area.

Services we provide:
Servicing, Repairs, Diagnostics, Clutches, Brakes, Exhaust for all makes and models of cars and vans.

10% discount for anyone who brings in this flyer with them.

Company contact details below:
Telephone 0151 4938271
Website www.kwbmotors-example.co.uk

Address
Unit 4 Harbour Workshops,
Millbeck Lane,
Glenworth Ind Estate,
Ellesmere Port,
CH65 8QX

Our Logo is attached

Target Market(s)

Local Residents and businesses

Industry/Entity Type

Auto Repair

Requirements
Must have
• Services we provide:
• Servicing, Repairs, Diagnostics, Clutches, Brakes, Exhaust for all makes and models of cars and vans.
• 10% discount for anyone who brings in this flyer with them.
• Company contact details below:
• Telephone 0151 4938271
• Website www.kwbmotors-example.co.uk
• Address
• Unit 4 Harbour Workshops,
• Millbeck Lane,
• Glenworth Ind Estate,
• Ellesmere Port,
• CH65 8QX

```html
<!DOCTYPE html>
<html lang="en">
<head>
<meta charset="utf-8">
<title>KWB Motors – A5 Leaflet</title>
<link rel="stylesheet" href="https://fonts.googleapis.com/css2?family=Open+Sans:wght@700;800&family=Varela+Round&display=swap">
<style>
  :root {
    --canvas-bg: #e8e3de;
    --paper: #ffffff;
    --brand-red: #e01b24;
    --brand-red-dark: #b3121a;
    --graphite: #3a3a3c;
    --graphite-light: #8a8a8c;
    --ink: #1c1c1c;
    --white: #ffffff;
  }
  * { box-sizing: border-box; margin: 0; padding: 0; }
  html, body {
    width: 1200px; height: 1200px; overflow: hidden;
    background: var(--canvas-bg);
  }
  .canvas {
    position: relative; width: 1200px; height: 1200px;
    display: flex; align-items: center; justify-content: center;
  }
  .leaflet {
    position: relative; width: 760px; height: 1075px;
    background: var(--paper); overflow: hidden;
    box-shadow: 0 6px 24px rgba(0,0,0,.18);
  }
  .engine-photo {
    position: absolute; left: 0; top: 0; width: 760px; height: 600px;
    background: radial-gradient(ellipse at 55% 40%, #d9d9d9 0%, #9c9c9c 45%, #4e4e4e 100%);
  }
  .leaflet-shapes { position: absolute; inset: 0; }
  .corner-label {
    position: absolute; left: 34px; top: 88px;
    font-family: "Open Sans", sans-serif; font-weight: 700;
    font-size: 26px; color: var(--white);
  }
  .brand-name {
    position: absolute; right: 70px; top: 40px;
    display: flex; align-items: center; gap: 12px;
    font-family: "Varela Round", sans-serif;
    font-size: 40px; color: var(--graphite);
  }
  .brand-dot { width: 18px; height: 18px; border-radius: 50%; background: var(--brand-red); }
  .discount {
    position: absolute; left: 0; width: 760px; top: 262px;
    text-align: center;
    font-family: "Open Sans", sans-serif; font-weight: 800;
    font-size: 27px; line-height: 1.2; letter-spacing: .5px;
    text-transform: uppercase; color: var(--white);
    text-shadow: 0 1px 3px rgba(0,0,0,.45);
  }
  .services {
    position: absolute; left: 0; width: 760px; top: 568px;
    text-align: center; font-family: "Varela Round", sans-serif;
  }
  .section-title { font-size: 36px; line-height: 1.3; color: var(--brand-red); font-weight: 400; -webkit-text-stroke: .6px var(--brand-red); }
  .service-list { list-style: none; font-size: 22px; line-height: 1.4; color: var(--ink); -webkit-text-stroke: .3px var(--ink); }
  .contact { margin-top: 24px; }
  .contact .section-title { font-size: 28px; }
  .contact address { font-style: normal; font-size: 16px; line-height: 1.3; color: var(--ink); }
  .website {
    position: absolute; left: 0; width: 760px; bottom: 48px;
    text-align: center; font-family: "Varela Round", sans-serif;
    font-size: 18px; letter-spacing: 6px; color: var(--white);
  }
</style>
</head>
<body>
<div class="canvas">
  <article class="leaflet">
    <div class="engine-photo" role="img" aria-label="Black and white close-up photograph of a car engine bay"></div>

    <svg class="leaflet-shapes" viewBox="0 0 760 1075" width="760" height="1075" aria-hidden="true">
      <defs>
        <linearGradient id="redBand" x1="0" y1="0" x2="1" y2="1">
          <stop offset="0" stop-color="#c4121b"/>
          <stop offset=".5" stop-color="#ee2a31"/>
          <stop offset="1" stop-color="#b3121a"/>
        </linearGradient>
        <linearGradient id="greyWedge" x1="0" y1="0" x2="1" y2="0">
          <stop offset="0" stop-color="#bdbdbd"/>
          <stop offset="1" stop-color="#3a3a3c"/>
        </linearGradient>
        <linearGradient id="cornerBand" x1="0" y1="0" x2="1" y2="0">
          <stop offset="0" stop-color="#2c2c2e"/>
          <stop offset="1" stop-color="#6a6a6c"/>
        </linearGradient>
      </defs>

      <path class="corner-band" d="M0,70 L360,10 L300,120 L0,160 Z" fill="url(#cornerBand)"/>
      <path class="logo-plate" d="M330,0 L760,0 L760,110 C620,90 470,100 330,110 Z" fill="#ffffff" opacity=".82"/>

      <path class="red-band" d="M0,440 C260,425 520,370 760,300 L760,440 C520,480 260,505 0,515 Z" fill="url(#redBand)"/>
      <path class="white-edge" d="M0,432 C260,417 520,362 760,292" fill="none" stroke="#ffffff" stroke-width="6"/>
      <path class="paper-area" d="M0,510 C260,500 520,475 760,435 L760,1075 L0,1075 Z" fill="#ffffff"/>
      <path class="grey-wedge" d="M300,545 C470,528 640,495 760,452 L760,420 C600,462 460,505 300,545 Z" fill="url(#greyWedge)"/>

      <path class="red-swoosh" d="M0,985 C250,968 520,925 760,865 L760,885 C520,945 260,995 0,1008 Z" fill="url(#redBand)"/>
      <path class="grey-swoosh" d="M0,1010 C260,998 520,962 760,905 L760,922 C520,978 260,1010 0,1020 Z" fill="#d6d6d6"/>
      <path class="footer-band" d="M0,1022 C260,1014 520,984 760,935 L760,1075 L0,1075 Z" fill="url(#redBand)"/>
    </svg>

    <div class="corner-label">KWB Motors</div>
    <div class="brand-name"><span>KWB Motors</span><span class="brand-dot"></span></div>

    <p class="discount">10% discount for anyone who brings<br>in this flyer with them</p>

    <section class="services">
      <h2 class="section-title">Services We Provide:</h2>
      <ul class="service-list">
        <li>• Servicing • Repairs • Diagnostics</li>
        <li>• Clutches • Brakes</li>
        <li>• Exhaust For All Makes • Models Of Cars And Vans</li>
      </ul>
      <div class="contact">
        <h3 class="section-title">Company contact :</h3>
        <address>
          0151 4938271<br>
          Unit 4 Harbour Workshops,<br>
          Millbeck Lane,<br>
          Glenworth Ind Estate,<br>
          Ellesmere Port,<br>
          CH65 8QX
        </address>
      </div>
    </section>

    <p class="website">www.kwbmotors-example.co.uk</p>
  </article>
</div>
</body>
</html>
```